KFZ-Gutachter Banner

Ziel des Banners:
Der Banner soll auf die Tätigkeit als Kfz-Sachverständiger aufmerksam machen. Er wird im Außenbereich eingesetzt und soll schon aus der Ferne verständlich und gut lesbar sein.

Gestaltung:
• Schlichtes, professionelles Design (keine überladene Gestaltung, ruhige Farbwahl – anlehnend an den Farben schwarz und Rot.
• Ein Bild wo sich zwei hochwertige Autos verunfallt befinden
• Großzügige Schriftgrößen – der Text muss auch aus 20–30 m Entfernung gut lesbar sein
• Klare Informationsstruktur

Inhalte (Text):
1. Überschrift / Hauptaussage (groß & auffällig):
Kfz-Sachverständiger
oder
Unfallgutachten vom Profi
2. Kurze Beschreibung (kleiner, aber lesbar):
• Unfallgutachten
• Fahrzeugbewertung
• Technische Beratung
3. Kontaktdaten (am wichtigsten – sehr gut sichtbar & lesbar):
• Telefonnummer (z. B. groß & fett)
• Website oder E-Mail
• Optional: Standort oder “auch mobil im Einsatz”

Bildelemente:
• Optional ein dezentes Symbol oder Icon (z. B. Auto, Lupe, Checkzeichen) – nur wenn es nicht vom Text ablenkt

Format:
• Querformat, je nach Platz vor Ort (z. B. 3 m x 1,5 m)

Ingenieurbüro Lorenz Vahle Ostlinger Str.14 58706 Menden www.pruefwerk-tz.de

• Man muss sofort erkennen, dass es sich um einen KFZ-Gutachter handelt.

```html
<!DOCTYPE html>
<html lang="de">
<head>
<meta charset="utf-8">
<title>Unfallgutachten vom Profi – Lorenz Vahle</title>
<link rel="stylesheet" href="https://fonts.googleapis.com/css2?family=League+Spartan:wght@400;700;800&family=Montserrat:wght@400;500&display=swap">
<style>
  :root {
    --bg: #e9edf1;
    --ink: #121720;
    --ink-soft: #1a2029;
    --red: #d21f30;
    --white: #f4f4f4;
    --grey: #d5d8dc;
  }
  * { margin: 0; padding: 0; box-sizing: border-box; }
  html, body { width: 1200px; height: 849px; overflow: hidden; background: var(--bg); }
  .banner {
    position: absolute; left: 30px; top: 145px; width: 1140px; height: 560px;
    background: linear-gradient(135deg, var(--ink-soft), var(--ink));
    font-family: "League Spartan", sans-serif; color: var(--white); overflow: hidden;
  }
  .brand { position: absolute; left: 40px; top: 40px; width: 200px; text-align: center; }
  .brand-name {
    display: flex; align-items: center; justify-content: center; gap: 8px;
    font-family: "Montserrat", sans-serif; font-weight: 500; font-size: 21px; letter-spacing: 2px;
  }
  .brand-mark { width: 10px; height: 10px; background: var(--red); }
  .brand-sub {
    margin-top: 10px; font-family: "Montserrat", sans-serif; font-size: 11.5px;
    letter-spacing: 1.6px; line-height: 1.6; color: var(--grey);
  }
  .headline {
    position: absolute; right: 58px; top: 22px; text-align: right;
    font-weight: 800; font-size: 84px; line-height: 0.98; letter-spacing: -1px; text-transform: uppercase;
  }
  .headline .accent { color: var(--red); }
  .ribbon { position: absolute; left: 43px; top: 206px; width: 462px; height: 56px; }
  .ribbon svg { position: absolute; inset: 0; }
  .ribbon-text {
    position: absolute; left: 20px; top: 0; height: 56px; display: flex; align-items: center;
    font-weight: 800; font-size: 31px; padding-top: 5px; letter-spacing: -0.3px;
  }
  .services { position: absolute; left: 18px; top: 295px; list-style: none; }
  .services li {
    display: flex; align-items: center; gap: 18px; height: 44.5px;
    font-weight: 700; font-size: 27px; text-transform: uppercase; padding-top: 4px; letter-spacing: -0.3px;
  }
  .services svg { width: 22px; height: 22px; margin-top: -4px; }
  .crash-photo {
    position: absolute; left: 470px; top: 222px; width: 645px; height: 222px;
    background: radial-gradient(ellipse at 50% 50%, #8e1d2a 0%, #2b3447 30%, #1a2130 60%, rgba(18,23,32,0) 80%);
  }
  .contact-band {
    position: absolute; left: 0; bottom: 0; width: 100%; height: 82px; background: var(--red);
    display: flex; align-items: center; font-weight: 800; font-size: 52px; padding-top: 6px;
  }
  .contact-item { position: absolute; display: flex; align-items: center; gap: 16px; }
  .contact-web { left: 55px; }
  .contact-phone { right: 48px; }
  .contact-item svg { width: 40px; height: 40px; margin-top: -6px; }
</style>
</head>
<body>
  <main class="banner">
    <div class="brand">
      <div class="brand-name"><span class="brand-mark"></span>LORENZ VAHLE</div>
      <div class="brand-sub">KFZ-SACHVERSTÄNDIGER<br>INGENIEURBÜRO</div>
    </div>

    <h1 class="headline">Unfallgutachten<br>vom <span class="accent">Profi</span></h1>

    <div class="ribbon">
      <svg viewBox="0 0 462 56" preserveAspectRatio="none"><polygon points="0,0 442,0 462,28 442,56 0,56" fill="var(--red)"/></svg>
      <span class="ribbon-text">AUCH MOBIL IM EINSATZ</span>
    </div>

    <ul class="services">
      <li><svg viewBox="0 0 24 24"><path d="M2 13 L9 20 L22 4" fill="none" stroke="var(--red)" stroke-width="4.5" stroke-linecap="round" stroke-linejoin="round"/></svg>Unfallgutachten</li>
      <li><svg viewBox="0 0 24 24"><path d="M2 13 L9 20 L22 4" fill="none" stroke="var(--red)" stroke-width="4.5" stroke-linecap="round" stroke-linejoin="round"/></svg>Fahrzeugbewertung</li>
      <li><svg viewBox="0 0 24 24"><path d="M2 13 L9 20 L22 4" fill="none" stroke="var(--red)" stroke-width="4.5" stroke-linecap="round" stroke-linejoin="round"/></svg>Technische</li>
    </ul>

    <div class="crash-photo" role="img" aria-label="Foto: zwei dunkelblaue Limousinen nach einem Frontalzusammenstoß vor einem roten Pinselstrich"></div>

    <footer class="contact-band">
      <div class="contact-item contact-web">
        <svg viewBox="0 0 40 40"><circle cx="20" cy="20" r="17" fill="none" stroke="var(--white)" stroke-width="4"/><path d="M4 20 H36 M20 3 C11 12 11 28 20 37 M20 3 C29 12 29 28 20 37" fill="none" stroke="var(--white)" stroke-width="3"/></svg>
        <span>WWW.SV-VAHLE.DE</span>
      </div>
      <div class="contact-item contact-phone">
        <svg viewBox="0 0 40 40"><circle cx="20" cy="20" r="19" fill="var(--white)"/><path d="M14 10 l4 5 -2.5 2.5 c1.5 3 4 5.5 7 7 L25 22 l5 4 -3 3.5 C19 29 11 21 10.5 13 Z" fill="var(--red)"/></svg>
        <span>02373-4417260</span>
      </div>
    </footer>
  </main>
</body>
</html>
```